Complete Website Redesign

We need a complete revamp of our website. Need to add interactive custmer catalog seection tools. Need to add customer spec input for recommended product search results. Need a cutomer lead and opportunity contact capability. Need a complete Branding message revamp. Primary visuals will be prodcut pictures and case studies.
Industrial Customers in the high durability Air movement and fan/blower space; high durability enclosure and flow industries ie. mining, chamicals, manufacturing, water treatment, chemical in use manufacturing

```html
<!DOCTYPE html>
<html lang="en">
<head>
<meta charset="utf-8">
<title>Durafil Composite Works, LLC</title>
<link rel="stylesheet" href="https://fonts.googleapis.com/css2?family=Ubuntu:wght@400;500;700&family=PT+Sans:wght@400;700&display=swap">
<style>
:root{
  --backdrop:#4d5a73;
  --header:#8d95a8;
  --brand:#2e2f8c;
  --nav-top:#ececec;
  --nav-bottom:#cdcdcd;
  --nav-text:#8a8a8a;
  --heading:#1a5d96;
  --text:#222;
  --panel-line:#cfcfcf;
  --bar-top:#3a3a3a;
  --bar-bottom:#0c0c0c;
  --footer:#3d4860;
  --footer-deep:#262c38;
  --footer-text:#e6e9ef;
  --link:#2a62b0;
}
*{box-sizing:border-box;margin:0;padding:0}
html,body{width:960px;height:1200px;overflow:hidden}
body{background:var(--backdrop);font-family:"PT Sans",sans-serif;color:var(--text);position:relative}
.page{position:absolute;left:171px;top:0;width:669px;height:1200px}
.site-header{position:absolute;left:0;top:0;width:669px;height:64px;background:var(--header)}
.brand{position:absolute;left:8px;top:17px;display:flex;align-items:center;gap:10px;font-family:"Ubuntu",sans-serif;font-weight:500;color:var(--brand);font-size:15px}
.brand-mark{width:30px;height:30px;border-radius:50%;background:var(--brand)}
.main-nav{position:absolute;left:0;top:64px;width:669px;height:45px;background:linear-gradient(var(--nav-top),var(--nav-bottom));font-family:"Ubuntu",sans-serif;font-size:12px}
.main-nav a{position:absolute;top:19px;color:var(--nav-text);text-decoration:none}
.main-nav a.current{color:#222}
.search-icon{position:absolute;left:620px;top:17px}
.hero{position:absolute;left:0;top:109px;width:669px;height:213px;background:linear-gradient(100deg,#dcdcdc 0%,#9a9a9a 45%,#3a3a3a 70%,#bdbdbd 100%)}
.content{position:absolute;left:0;top:322px;width:669px;height:593px;background:#fff}
.intro h1,.intro h2{font-family:"Ubuntu",sans-serif;font-weight:700;color:var(--heading);font-size:19px;position:absolute;left:18px}
.intro p{position:absolute;left:18px;width:490px;font-size:11px;line-height:18px}
.product-title{position:absolute;font-family:"Ubuntu",sans-serif;font-weight:500;font-size:12px;color:var(--heading);white-space:nowrap}
.product-card{position:absolute;width:148px;height:111px;border:1px solid var(--panel-line);background:#fff}
.product-photo{position:absolute;left:44px;top:10px;width:60px;height:58px;background:radial-gradient(circle,#b9bdc4,#eef0f2);border-radius:4px}
.product-card ul{position:absolute;left:8px;list-style:none;font-size:8px;line-height:17px}
.product-card li::before{content:"";display:inline-block;border-left:5px solid #111;border-top:3.5px solid transparent;border-bottom:3.5px solid transparent;margin-right:8px}
.side-panel{position:absolute;left:520px;width:142px;border:1px solid var(--panel-line);background:#fff}
.side-panel h3{height:23px;background:linear-gradient(var(--bar-top),var(--bar-bottom));color:#fff;font-family:"Ubuntu",sans-serif;font-size:13px;font-weight:700;text-align:center;line-height:23px}
.field{position:absolute;left:8px;font-size:10px;display:flex;width:128px;justify-content:space-between;align-items:center}
.field span{display:block;width:79px;height:14px;border:1px solid #ccc}
.dark-btn{position:absolute;background:#111;color:#fff;font-family:"Ubuntu",sans-serif;border-radius:3px;text-align:center}
.case-list{list-style:none;padding:7px 3px 0 4px;font-size:8.5px;line-height:12px}
.case-list li{display:flex;gap:5px;margin-bottom:6px}
.case-list li::before{content:"";flex:none;margin-top:2px;border-left:5px solid #111;border-top:3.5px solid transparent;border-bottom:3.5px solid transparent}
.case-list a{color:var(--link);text-decoration:none}
.site-footer{position:absolute;left:0;top:915px;width:669px;height:240px;background:var(--footer);color:var(--footer-text)}
.footer-head{position:absolute;font-family:"Ubuntu",sans-serif;font-size:12px}
.footer-list{position:absolute;list-style:none;font-size:8px;line-height:20px}
.footer-list li::before{content:"";display:inline-block;border-left:4px solid var(--footer-text);border-top:3px solid transparent;border-bottom:3px solid transparent;margin-right:8px}
.footer-list.social li::before{width:11px;height:11px;border:0;background:#8ea3c2;vertical-align:-2px;margin-right:8px}
.footer-text{position:absolute;font-size:8px;line-height:18px}
.email-input{position:absolute;left:210px;top:183px;width:152px;height:18px;background:var(--footer-deep);font-size:8px;line-height:18px;padding-left:8px}
.subscribe{position:absolute;left:212px;top:211px;width:66px;height:18px;background:#14171d;border:1px solid #555;font-size:7.5px;text-align:center;line-height:16px}
.copyright{position:absolute;left:0;top:1155px;width:669px;height:45px;background:var(--footer-deep);color:var(--footer-text);font-family:"Ubuntu",sans-serif;font-size:11px;text-align:center;line-height:45px}
</style>
</head>
<body>
<div class="page">
  <header class="site-header">
    <div class="brand"><span class="brand-mark"></span>DCW Durafil Composite Works, LLC</div>
  </header>
  <nav class="main-nav">
    <a class="current" style="left:38px">Home</a>
    <a style="left:97px">Products</a>
    <a style="left:164px">About Us</a>
    <a style="left:232px">Mission</a>
    <a style="left:291px">Request Information</a>
    <a style="left:420px">Contacts</a>
    <svg class="search-icon" width="14" height="14" viewBox="0 0 14 14"><circle cx="5.5" cy="5.5" r="4" fill="none" stroke="#111" stroke-width="2"/><line x1="8.5" y1="8.5" x2="13" y2="13" stroke="#111" stroke-width="2.4"/></svg>
  </nav>
  <div class="hero" role="img" aria-label="Close-up photograph of a black fiberglass axial fan propeller with a metal hub"></div>

  <main class="content">
    <section class="intro">
      <h1 style="top:22px">Welcome to DCW</h1>
      <p style="top:62px">Here at Durafil Composite Works, LLC., we are focused on continuous improvement of our operation. Our objective and vision is to capture more market share geographically while serving the petrochemical, military, industrial and construction markets and grow our presence in the energy industry.</p>
      <h2 style="top:135px">Our Mission</h2>
      <p style="top:174px">Durafil Composite Works, LLC., located in Ashford, New York manufactures corrosion resistant fiberglass Purification and Dust Collection Equipment. DCW is a new name with a new face dedicated to meeting the changing needs of individual customers. Our mission has been to deliver existing quality products, improving upon an existing fiberglass design of both standard and custom products while collectively giving superior customer service.</p>
    </section>

    <h4 class="product-title" style="left:14px;top:291px">Fiberglass Axial Propellers</h4>
    <div class="product-card" style="left:14px;top:309px">
      <div class="product-photo" role="img" aria-label="Fan propeller product photo"></div>
      <ul style="top:82px"><li>Fan Propellers</li></ul>
    </div>
    <h4 class="product-title" style="left:188px;top:291px">Fiberglass Axial Fans</h4>
    <div class="product-card" style="left:188px;top:309px">
      <div class="product-photo" role="img" aria-label="Tubeaxial duct fan product photo"></div>
      <ul style="top:72px"><li>Tubeaxial Duct Fan</li><li>Wall Box Fan</li></ul>
    </div>
    <h4 class="product-title" style="left:363px;top:291px">Fiberglass Centrifugal Fans</h4>
    <div class="product-card" style="left:363px;top:309px">
      <div class="product-photo" role="img" aria-label="Centrifugal blower product photo"></div>
      <ul style="top:71px;left:4px"><li>Backward Incline Centrifugal Blower</li><li>Radial Centrifugal Blower</li></ul>
    </div>
    <h4 class="product-title" style="left:102px;top:440px">Louvers and Dampers</h4>
    <div class="product-card" style="left:102px;top:459px">
      <div class="product-photo" role="img" aria-label="Round damper product photo"></div>
      <ul style="top:72px;left:4px"><li>6" Adjustable Louvers and Dampers</li><li>Round Dampers</li></ul>
    </div>
    <h4 class="product-title" style="left:313px;top:440px">High Plume Exhaust Fans</h4>
    <div class="product-card" style="left:313px;top:459px">
      <div class="product-photo" role="img" aria-label="High plume exhauster product photo"></div>
      <ul style="top:84px;left:18px"><li>High Plume Exhausters</li></ul>
    </div>

    <aside class="side-panel" style="top:26px;height:185px">
      <h3>Product Search</h3>
      <div class="field" style="top:43px">Product<span></span></div>
      <div class="field" style="top:63px">Blades<span></span></div>
      <div class="field" style="top:83px">Diameter<span></span></div>
      <div class="field" style="top:102px">Hub Size<span></span></div>
      <div class="field" style="top:122px">Remarks<span></span></div>
      <div class="dark-btn" style="left:74px;top:151px;width:60px;height:22px;font-size:12px;line-height:22px">Search</div>
    </aside>
    <aside class="side-panel" style="top:308px;height:93px">
      <h3>Case Study</h3>
      <ul class="case-list">
        <li><span>Lorem ipsum dolor sit amet, consectetur. <a>Read more...</a></span></li>
        <li><span>Nullam fringilla lacus vitae diam varius non.<a>Read more...</a></span></li>
      </ul>
    </aside>
    <aside class="side-panel" style="top:435px;height:135px">
      <h3>FeedBack</h3>
      <div class="field" style="top:32px">Name<span></span></div>
      <div class="field" style="top:57px">Email<span></span></div>
      <div class="field" style="top:79px;align-items:flex-start">Massage<span style="height:37px;margin-top:-5px"></span></div>
      <div class="dark-btn" style="left:92px;top:119px;width:40px;height:14px;font-size:10px;line-height:14px;border-radius:1px">Submit</div>
    </aside>
  </main>

  <footer class="site-footer">
    <div class="footer-head" style="left:53px;top:24px">Address</div>
    <div class="footer-text" style="left:53px;top:47px">Durafil Composite Works, LLC<br>27 Mill Row / P.O. Box 118<br>Ashford, NY 14000</div>
    <div style="position:absolute;left:53px;top:108px;display:flex;align-items:center;gap:6px;font-size:12px">
      <svg width="10" height="13" viewBox="0 0 10 13"><path d="M2 0h2l1 3-1.5 1.5c.6 1.8 1.6 3 3 4L8 7l2 2v2l-2 2C3 11 0 6 0 2z" fill="#e6e9ef"/></svg>555-014-2290</div>
    <div style="position:absolute;left:53px;top:139px;display:flex;align-items:center;gap:4px;font-size:8px">
      <svg width="15" height="11" viewBox="0 0 15 11"><rect x=".5" y=".5" width="14" height="10" fill="#e6e9ef"/><path d="M.5 .5l7 6 7-6" fill="none" stroke="#3d4860"/></svg>sales@durafilcw.example</div>

    <div class="footer-head" style="left:210px;top:24px">Help And Support</div>
    <ul class="footer-list" style="left:210px;top:42px"><li>Lorem ipsum</li><li>Donec scelerisque</li><li>Quisque tempor</li><li>Cras venenatis</li></ul>
    <div class="footer-head" style="left:210px;top:139px">NEWSLETTER SIGNUP</div>
    <div class="footer-text" style="left:210px;top:160px">Enter Your Email to join mailing list</div>
    <div class="email-input">E-mail Address</div>
    <div class="subscribe">SUBSCRIBE</div>

    <div class="footer-head" style="left:397px;top:24px">LINK TO US</div>
    <ul class="footer-list social" style="left:397px;top:42px"><li>Chirp</li><li>Bookmarks</li><li>Friendbook</li><li>Rss</li></ul>
    <div class="footer-head" style="left:397px;top:139px">FOR CLIENTS</div>
    <ul class="footer-list" style="left:397px;top:158px"><li>Signup</li><li>Blog</li><li>Promotions</li></ul>

    <div class="footer-head" style="left:514px;top:24px">COMPANY</div>
    <ul class="footer-list" style="left:514px;top:42px"><li>Lorem ipsum</li><li>Donec scelerisque</li><li>Quisque tempor</li><li>Cras venenatis</li></ul>
    <div class="footer-head" style="left:514px;top:139px">TESTIMONIAL</div>
    <div class="footer-text" style="left:514px;top:158px">Lorem ipsum dolor sit amet,<br>consectetur adipiscing elit.<br>Sed euismod neque gravida<br>laoreet.</div>
  </footer>
  <div class="copyright">Copyright © 2013 Durafil composite works</div>
</div>
</body>
</html>
```